Fence Contractor Website Design

We are working with Yardline Works. They are a local fencing and automatic gate installer and in need of a new website design.
Some sites to use for inspiration:
https://pinevalebarrier.example
https://marwickrails.example
https://www.tellurpostsandboards.example
https://www.grovanpaneling.example
Thank you for taking the time to consider designing a website for us. We are web developers based in Stockton, CA, USA. Most of our projects go through the same process. Understanding this process may help you win a project with us. We custom-code all of our websites in-house. We don’t have any requirements as to what tools you use for your design, but we prefer Figma files. For any design that we label as four-stars, we send it to the client for review. The client picks the final design they want us to use. Once we complete this process, we will continue to show additional clients all the four-star sites and purchase them later. Your designs will have multiple chances to sell. For better chances of success, we ask that you follow these guidelines.
IMAGES:
If you use any images or icons in the design, we ask that you have a link to the asset so we can purchase the image/icon. Most of the designs we submit do not have the customer’s images on them unless they have some great images. Be creative; show us the feeling you are trying to portray with your image choices. Use any royalty-free site you choose. We subscribe to Stockvane and mainly use their images, but we can purchase images outside of Stockvane.
PLEASE NOTE: we will not submit designs to clients with watermarks on the images.
FONTS:
We ask that you identify the fonts used in the design. This can be done in a message if you want. We typically use Google Fonts and Stockvane Fonts.
CONTENT:
We're always open to different content and ideas. We often submit designs with stock images so the client can see our vision. We typically take pictures after the website launch to use their images with our vision. Lorem Ipsum is fine for paragraphs, but we ask that you write the headers in correct English. We want to be able to show the vision and identify the sections of the website.
INSPIRATION:
We typically add a couple of links in the brief of websites we like to help you get started in your design.
REVISIONS:
We do not often ask for revisions of the designs unless we see something in the design that may not appeal to the client. If there are slight changes that we want to make, we do that in the development process.
FEEDBACK:
We rarely give feedback on designs during the design process. We are working on many website projects and do not have the time to provide feedback. We usually respond if your request is well thought out and asks specific questions, but a note asking “feedback, please” usually goes unanswered.
Number of Pages Required
1 page
Look and feel
Each slider illustrates characteristics of the customer's brand and the style your logo design should communicate.

```html
<!DOCTYPE html>
<html lang="en">
<head>
<meta charset="utf-8">
<title>Yardline Works Fencing &amp; Gates</title>
<link href="https://fonts.googleapis.com/css2?family=Russo+One&family=Open+Sans:wght@400;600;700;800&display=swap" rel="stylesheet">
<style>
:root{
  --navy:#1c2846;
  --navy-dark:#16203a;
  --red:#ee1b1b;
  --red-deep:#b80d0d;
  --grey:#ededed;
  --card-grey:#f2f2f2;
  --text:#6b6b6b;
  --white:#ffffff;
}
*{box-sizing:border-box;margin:0;padding:0}
html,body{width:1200px;height:5093px;overflow:hidden}
body{position:relative;font-family:"Open Sans",Arial,sans-serif;color:var(--text);background:var(--white)}
.abs{position:absolute}
.display{font-family:"Russo One","Arial Black",sans-serif;color:var(--navy);text-transform:uppercase;letter-spacing:1px}
.display .accent{color:var(--red)}
.btn{position:absolute;display:flex;align-items:center;justify-content:center;background:var(--red);color:var(--white);font-family:"Open Sans",Arial,sans-serif;font-weight:800;font-size:14px;text-transform:uppercase;letter-spacing:.5px}
.brand-word{font-family:"Russo One","Arial Black",sans-serif;text-transform:uppercase;line-height:1;white-space:nowrap}

/* header */
.site-header{position:absolute;left:0;top:0;width:1200px;height:113px;background:var(--white)}
.header-logo{left:60px;top:30px;font-size:24px;color:var(--navy);display:flex;align-items:center;gap:10px}
.header-logo .dot{width:22px;height:22px;background:var(--red)}
.topbar-call{left:613px;top:0;width:308px;height:36px;background:var(--red);color:var(--white);font-size:14px;display:flex;align-items:center;justify-content:center;gap:10px}
.topbar-call b{font-weight:800;letter-spacing:1px}
.topbar-quote{left:929px;top:0;width:211px;height:36px;background:var(--navy);color:var(--white);font-weight:800;font-size:14px;display:flex;align-items:center;justify-content:center;letter-spacing:.5px}
.main-nav{left:378px;top:54px;display:flex;gap:0;font-size:14px;text-transform:uppercase}
.main-nav a{color:#555;text-decoration:none;padding:0 16px;height:42px;display:flex;align-items:center}
.main-nav a.active{background:var(--navy);color:var(--white)}

/* hero */
.hero{left:0;top:113px;width:1200px;height:674px;background:linear-gradient(100deg,#1d2a4c 0%,#2a3656 35%,#5a5a55 65%,#8a7a58 85%,#3a3526 100%)}
.hero-title{left:60px;top:250px;font-size:38px;color:var(--white);line-height:46px}
.hero-text{left:60px;top:352px;width:600px;font-size:14px;line-height:30px;color:var(--white)}
.hero .btn{left:60px;top:443px;width:177px;height:51px}

/* about */
.about{left:0;top:787px;width:1200px;height:492px;text-align:center}
.about-mark{left:450px;top:90px;width:300px;font-size:20px;color:var(--navy);display:flex;flex-direction:column;align-items:center;gap:8px}
.about-mark .dot{width:22px;height:22px;background:var(--red)}
.about h2{position:absolute;left:0;width:1200px;top:186px;font-size:36px}
.about p{position:absolute;left:210px;width:780px;top:257px;font-size:14px;line-height:26px}
.about .btn{left:522px;top:363px;width:156px;height:52px}

/* services */
.services{left:0;top:1279px;width:1200px;height:1163px;background:var(--grey)}
.section-title{position:absolute;left:0;width:1200px;text-align:center;font-size:36px}
.service-card{position:absolute;width:331px;height:441px;background:var(--white);text-align:center}
.service-card .photo{height:225px}
.service-card h3{margin-top:26px;font-family:"Russo One",sans-serif;font-weight:400;font-size:17px;color:#1b1b1b;letter-spacing:1px}
.service-card p{margin:22px auto 0;width:270px;font-size:13px;line-height:26px}
.service-card .btn{left:95px;top:364px;width:142px;height:44px;font-size:13px}

/* build cta */
.build{left:0;top:2442px;width:1200px;height:381px;background:radial-gradient(ellipse at 50% 40%,#e01e1e 0%,#c41010 55%,#9c0a0a 100%);text-align:center;color:var(--white)}
.build h2{position:absolute;left:0;width:1200px;top:50px;font-size:36px;color:var(--white)}
.build p{position:absolute;left:210px;width:780px;top:104px;font-size:13px;line-height:26px}
.build-phone{position:absolute;left:0;width:1200px;top:170px;display:flex;justify-content:center;align-items:center;gap:14px;font-family:"Russo One",sans-serif;font-size:32px}
.build-phone .ring{width:52px;height:52px;border-radius:50%;background:var(--white);display:flex;align-items:center;justify-content:center}
.build .btn{left:433px;top:255px;width:334px;height:51px;background:var(--white);color:var(--navy)}

/* testimonials */
.testimonials{left:0;top:2823px;width:1200px;height:552px}
.quote-card{position:absolute;top:158px;width:247px;height:261px;background:var(--card-grey);padding:42px 18px 0 18px}
.quote-card .badge{position:absolute;left:14px;top:-16px;width:40px;height:40px;border-radius:50%;background:var(--red);color:var(--white);font-family:Georgia,serif;font-weight:700;font-size:30px;line-height:50px;text-align:center}
.quote-card p{font-size:13px;line-height:26px}
.quote-card .client{margin-top:20px;font-weight:700;font-size:13px;color:var(--navy)}
.quote-card .stars{margin-top:4px;color:#f5a623;font-size:15px;letter-spacing:1px}
.dots{left:560px;top:460px;display:flex;gap:12px}
.dots span{width:12px;height:12px;border-radius:50%;border:1.5px solid var(--navy)}
.dots span.on{background:var(--navy)}

/* gallery */
.gallery{left:0;top:3375px;width:1200px;height:678px;background:var(--grey)}
.tile{position:absolute}

/* areas */
.areas{left:0;top:4053px;width:1200px;height:520px}
.areas h2{position:absolute;left:60px;top:82px;font-size:36px}
.area-box{position:absolute;width:240px;height:52px;background:var(--grey);font-size:13px;color:#333;display:flex;align-items:center;padding-left:20px}
.area-box.active{background:var(--navy);color:var(--white)}

/* footer */
.footer{left:0;top:4662px;width:1200px;height:431px;background:var(--navy);color:var(--white)}
.start-box{left:59px;top:4573px;width:1080px;height:178px;background:var(--red)}
.start-box h2{position:absolute;left:52px;top:38px;font-size:36px;line-height:52px;color:var(--white)}
.start-box .btn{left:870px;top:54px;width:160px;height:46px;background:var(--navy);font-size:13px}
.footer-logo{left:60px;top:190px;font-size:22px;color:var(--white);display:flex;align-items:center;gap:10px}
.footer-logo .dot{width:20px;height:20px;background:var(--red)}
.footer-col{position:absolute;top:130px;font-size:13px}
.footer-col h4{font-family:"Open Sans",sans-serif;font-weight:800;font-size:13px;margin-bottom:18px}
.footer-col li{list-style:none;line-height:26px}
.contact-line{display:flex;gap:14px;line-height:26px;margin-bottom:18px}
.contact-line svg{flex:none;margin-top:5px}
.copyright{left:60px;top:393px;font-size:13px}
.socials{left:1035px;top:390px;display:flex;gap:26px}
.socials span{width:18px;height:18px;border-radius:50%;background:var(--red)}
</style>
</head>
<body>

<header class="site-header">
  <div class="abs header-logo brand-word"><span class="dot"></span>Yardline Works</div>
  <div class="abs topbar-call">CALL US AT
    <svg width="18" height="18" viewBox="0 0 24 24" aria-hidden="true"><path fill="#fff" d="M6.6 10.8a15.2 15.2 0 0 0 6.6 6.6l2.2-2.2c.3-.3.7-.4 1-.2 1.1.4 2.3.6 3.6.6.6 0 1 .4 1 1V20c0 .6-.4 1-1 1A17 17 0 0 1 3 4c0-.6.4-1 1-1h3.5c.6 0 1 .4 1 1 0 1.3.2 2.5.6 3.6.1.3 0 .7-.2 1z"/></svg>
    <b>+ 123 456 7890</b></div>
  <div class="abs topbar-quote">GET A FREE QUOTE</div>
  <nav class="abs main-nav">
    <a class="active">Home</a><a>About</a><a>Services</a><a>Areas We Serviceserved</a><a>Gallery</a><a>Reviews</a><a>Contact</a>
  </nav>
</header>

<section class="abs hero" role="img" aria-label="Photo of a dark metal fence line receding into a sunset-lit field">
  <svg class="abs" style="left:60px;top:162px" width="74" height="72" viewBox="0 0 24 24" aria-hidden="true"><path fill="#fff" d="M12 1.5l3.1 7 7.6.7-5.8 5 1.8 7.4L12 17.7 5.3 21.6l1.8-7.4-5.8-5 7.6-.7z"/></svg>
  <h1 class="abs display hero-title">Lakeshore and Northwoods<br>Yardline Works Fencing &amp; Gates</h1>
  <p class="abs hero-text">Lorem Ipsum is simply dummy text of the printing and typesetting industry. Lorem Ipsum has been the industry's standard dummy text ever since the 1500</p>
  <div class="btn">Free Estimate</div>
</section>

<section class="abs about">
  <div class="abs about-mark brand-word"><span class="dot"></span>Yardline Works</div>
  <h2 class="display">About Yardline Works <span class="accent">Fencing and Gates</span></h2>
  <p>Lorem Ipsum is simply dummy text of the printing and typesetting industry. Lorem Ipsum has been the industry's standard dummy text ever since the 1500s, when an unknown printer took a galley of type and scrambled it to make a type specimen book. It has survived not only five centuries, but also the leap into electronic</p>
  <div class="btn">Learn More</div>
</section>

<section class="abs services">
  <h2 class="display section-title" style="top:74px">Service <span class="accent">We Provide</span></h2>

  <article class="service-card" style="left:59px;top:164px">
    <div class="photo" role="img" aria-label="Photo of a white composite picket fence" style="background:linear-gradient(160deg,#5d7a2a 0%,#d9dcd2 35%,#eceee8 100%)"></div>
    <h3>Composite Fencing</h3>
    <p>Lorem Ipsum is simply dummy text of the printing and typesetting industry.</p>
    <div class="btn">Learn More</div>
  </article>
  <article class="service-card" style="left:435px;top:164px">
    <div class="photo" role="img" aria-label="Photo of green ornamental iron fence spears" style="background:linear-gradient(180deg,#c9d3c4 0%,#3f6a3e 55%,#1f3b22 100%)"></div>
    <h3>Ornamental Iron Fences</h3>
    <p>Lorem Ipsum is simply dummy text of the printing and typesetting industry.</p>
    <div class="btn">Learn More</div>
  </article>
  <article class="service-card" style="left:810px;top:164px">
    <div class="photo" role="img" aria-label="Photo of a rustic wooden rail fence on grass" style="background:linear-gradient(170deg,#a9b29a 0%,#6f8e3a 50%,#4c6e22 100%)"></div>
    <h3>Wood Fencing</h3>
    <p>Lorem Ipsum is simply dummy text of the printing and typesetting industry.</p>
    <div class="btn">Learn More</div>
  </article>

  <article class="service-card" style="left:59px;top:645px">
    <div class="photo" role="img" aria-label="Photo of barbed wire security fencing against a pale sky" style="background:linear-gradient(180deg,#e7e7e7 0%,#bdbdbd 60%,#4a4a4a 100%)"></div>
    <h3>Security Fences</h3>
    <p>Lorem Ipsum is simply dummy text of the printing and typesetting industry.</p>
  </article>
  <article class="service-card" style="left:435px;top:645px">
    <div class="photo" role="img" aria-label="Photo of a black aluminum fence with arched panels" style="background:linear-gradient(180deg,#8a8f76 0%,#6d7060 45%,#2a2b26 100%)"></div>
    <h3>Aluminum Fences</h3>
    <p>Lorem Ipsum is simply dummy text of the printing and typesetting industry.</p>
    <div class="btn">Learn More</div>
  </article>
  <article class="service-card" style="left:810px;top:645px">
    <div class="photo" role="img" aria-label="Photo of an open black iron double gate" style="background:linear-gradient(180deg,#f4f4f4 0%,#d8d8d8 50%,#2a2a2a 100%)"></div>
    <h3>Gate</h3>
    <p>Lorem Ipsum is simply dummy text of the printing and typesetting industry.</p>
    <div class="btn">Learn More</div>
  </article>
</section>

<section class="abs build" role="img" aria-label="Photo of a wrought iron fence against a red backdrop">
  <h2 class="display">Build Your Fence Today</h2>
  <p>Lorem Ipsum is simply dummy text of the printing and typesetting industry. Lorem Ipsum has been the industry's standard dummy text ever since the 1500s, when an unknown printer took a galley.</p>
  <div class="build-phone">
    <span class="ring"><svg width="24" height="24" viewBox="0 0 24 24" aria-hidden="true"><path fill="#1c2846" d="M6.6 10.8a15.2 15.2 0 0 0 6.6 6.6l2.2-2.2c.3-.3.7-.4 1-.2 1.1.4 2.3.6 3.6.6.6 0 1 .4 1 1V20c0 .6-.4 1-1 1A17 17 0 0 1 3 4c0-.6.4-1 1-1h3.5c.6 0 1 .4 1 1 0 1.3.2 2.5.6 3.6.1.3 0 .7-.2 1z"/></svg></span>
    + 123 456 7890
  </div>
  <div class="btn">Request a Free Estimate Today</div>
</section>

<section class="abs testimonials">
  <h2 class="display section-title" style="top:76px">What Our <span class="accent">Clients Say</span></h2>
  <article class="quote-card" style="left:59px"><span class="badge">&ldquo;</span><p>Lorem Ipsum is simply dummy text of the printing and typesetting industry. Lorem Ipsum has been the industry's standard dummy text.</p><div class="client">Client Name</div><div class="stars">★★★★★</div></article>
  <article class="quote-card" style="left:337px"><span class="badge">&ldquo;</span><p>Lorem Ipsum is simply dummy text of the printing and typesetting industry. Lorem Ipsum has been the industry's standard dummy text.</p><div class="client">Client Name</div><div class="stars">★★★★★</div></article>
  <article class="quote-card" style="left:615px"><span class="badge">&ldquo;</span><p>Lorem Ipsum is simply dummy text of the printing and typesetting industry. Lorem Ipsum has been the industry's standard dummy text.</p><div class="client">Client Name</div><div class="stars">★★★★★</div></article>
  <article class="quote-card" style="left:892px"><span class="badge">&ldquo;</span><p>Lorem Ipsum is simply dummy text of the printing and typesetting industry. Lorem Ipsum has been the industry's standard dummy text.</p><div class="client">Client Name</div><div class="stars">★★★★★</div></article>
  <div class="abs dots"><span class="on"></span><span></span><span></span><span></span></div>
</section>

<section class="abs gallery">
  <h2 class="display section-title" style="top:76px">Latest <span class="accent">Gallery</span></h2>
  <div class="tile" role="img" aria-label="Photo of an ornate wrought iron gate" style="left:59px;top:156px;width:331px;height:449px;background:linear-gradient(90deg,#3b2418 0%,#8a6a52 45%,#c2a98e 60%,#3a2418 100%)"></div>
  <div class="tile" role="img" aria-label="Photo of black iron fence spears in a garden" style="left:411px;top:156px;width:301px;height:214px;background:linear-gradient(180deg,#9fb08a 0%,#4d6a34 60%,#2a3a20 100%)"></div>
  <div class="tile" role="img" aria-label="Photo of a curled iron fence top in greenery" style="left:728px;top:156px;width:411px;height:214px;background:linear-gradient(160deg,#4f6a34 0%,#7c8a52 50%,#3b4a26 100%)"></div>
  <div class="tile" role="img" aria-label="Photo of a chain link fence at sunset" style="left:411px;top:391px;width:301px;height:214px;background:linear-gradient(180deg,#2b2414 0%,#8a6a2a 55%,#3a2c12 100%)"></div>
  <div class="tile" role="img" aria-label="Black and white photo of a picket fence silhouette" style="left:728px;top:391px;width:197px;height:214px;background:linear-gradient(180deg,#e6e6e6 0%,#9c9c9c 50%,#111 100%)"></div>
  <div class="tile" role="img" aria-label="Photo of a scrolled iron fence detail" style="left:941px;top:391px;width:198px;height:214px;background:linear-gradient(120deg,#7e8a4a 0%,#bfb58a 45%,#3a1e14 100%)"></div>
</section>

<section class="abs areas">
  <h2 class="display">Areas <span class="accent">We Serve</span></h2>
  <div class="area-box active" style="left:59px;top:166px">Area Name</div>
  <div class="area-box" style="left:322px;top:166px">Area Name</div>
  <div class="area-box" style="left:59px;top:241px">Area Name</div>
  <div class="area-box" style="left:322px;top:241px">Area Name</div>
  <div class="area-box" style="left:59px;top:316px">Area Name</div>
  <div class="area-box" style="left:322px;top:316px">Area Name</div>
  <div class="area-box" style="left:59px;top:391px">Area Name</div>
  <div class="area-box" style="left:322px;top:391px">Area Name</div>
  <div class="abs" role="img" aria-label="Dotted map of the service region with red location pins" style="left:643px;top:178px;width:454px;height:241px;background:radial-gradient(ellipse at 50% 50%,#d2d2d2 0%,#e6e6e6 55%,#ffffff 72%)"></div>
</section>

<footer class="abs footer">
  <div class="abs footer-logo brand-word"><span class="dot"></span>Yardline Works</div>
  <div class="footer-col" style="left:340px">
    <h4>Useful Links</h4>
    <ul><li>Home</li><li>About</li><li>Services</li><li>Areas we served</li><li>Gallery</li><li>Reviews</li><li>Contact</li></ul>
  </div>
  <div class="footer-col" style="left:617px">
    <h4>Other Service</h4>
    <ul><li>Gate Installation</li><li>Gate Operators</li><li>Access Control</li></ul>
  </div>
  <div class="footer-col" style="left:894px;width:250px">
    <h4>Contact Info</h4>
    <div class="contact-line"><svg width="14" height="16" viewBox="0 0 24 24" aria-hidden="true"><path fill="#ee1b1b" d="M12 2a7 7 0 0 0-7 7c0 5 7 13 7 13s7-8 7-13a7 7 0 0 0-7-7zm0 9.5A2.5 2.5 0 1 1 12 6.5a2.5 2.5 0 0 1 0 5z"/></svg><span>Lorem Ipsum is simply dummy text of the printing.</span></div>
    <div class="contact-line"><svg width="14" height="14" viewBox="0 0 24 24" aria-hidden="true"><path fill="#ee1b1b" d="M6.6 10.8a15.2 15.2 0 0 0 6.6 6.6l2.2-2.2c.3-.3.7-.4 1-.2 1.1.4 2.3.6 3.6.6.6 0 1 .4 1 1V20c0 .6-.4 1-1 1A17 17 0 0 1 3 4c0-.6.4-1 1-1h3.5c.6 0 1 .4 1 1 0 1.3.2 2.5.6 3.6.1.3 0 .7-.2 1z"/></svg><span>123 456 7890</span></div>
    <div class="contact-line"><svg width="16" height="12" viewBox="0 0 24 18" aria-hidden="true"><rect width="24" height="18" rx="2" fill="#ee1b1b"/><path d="M2 2l10 8 10-8" stroke="#1c2846" stroke-width="2" fill="none"/></svg><span>info@yardlineworks.example</span></div>
  </div>
  <div class="abs copyright">© Yardline Works Fencing &amp; Gates - 2025. Al Rights Reserved.</div>
  <div class="abs socials"><span></span><span></span><span></span></div>
</footer>

<div class="abs start-box">
  <h2 class="display">Let's Get Started On Your<br>Project Today</h2>
  <div class="btn">Free Estimate</div>
</div>

</body>
</html>
```